Need Powerpoint masters for my consulting company in privacy (RGPD) and IT

For my newly created consulting company I need powerpoint slides masters.
The company is specialzed in privacy (RGPD) and IT.
The company already has a logo (obtained via Marquelane).
These master slides will be mainly used when presenting reports/analysis to clients.
I'll attach a PNG files of the logo.

```html
<!DOCTYPE html>
<html lang="en">
<head>
<meta charset="utf-8">
<title>Lucien Moreau Conseil – Slide Masters</title>
<link rel="stylesheet" href="https://fonts.googleapis.com/css2?family=Montserrat:wght@300;400;500;600;700;800&family=Comfortaa:wght@400&display=swap">
<style>
:root{
  --teal:#0e7f8e;
  --teal-light:#1496a3;
  --navy:#0b2e48;
  --navy-deep:#082236;
  --ink:#16324a;
  --grey:#7a7a7a;
  --grey-light:#e8ecee;
  --text:#555;
  --canvas:#dcdcdc;
}
*{box-sizing:border-box;margin:0;padding:0}
html,body{width:790px;height:1200px;overflow:hidden;background:var(--canvas);font-family:"Montserrat",sans-serif;color:var(--ink)}
.sheet{position:relative;width:790px;height:1200px}
.slide{position:absolute;width:255px;height:143px;overflow:hidden;background:#fff}
.a{position:absolute}
.photo{position:absolute}
.brand{position:absolute;font-weight:500;font-size:4.2px;letter-spacing:.2px;display:flex;align-items:center;gap:2px;white-space:nowrap}
.brand i{display:block;width:5px;height:5px;background:currentColor}
.mini-mark{position:absolute;left:4px;top:4px;display:flex;align-items:center;gap:1px;font-size:2.2px;font-weight:600;color:var(--navy)}
.mini-mark i{display:block;width:4px;height:4px;background:var(--navy)}
.side-rule{position:absolute;left:12.5px;top:0;bottom:0;width:.6px;background:#e6e6e6}
.side-label{position:absolute;left:5px;top:46px;writing-mode:vertical-rl;transform:rotate(180deg);font-size:2.1px;letter-spacing:.4px;color:#b8c2c8;font-weight:600}
.page-no{position:absolute;left:5px;bottom:3px;font-size:2.4px;color:var(--ink)}
.s-title{position:absolute;font-weight:600;color:var(--ink);white-space:nowrap}
.center{left:0;right:0;text-align:center}
.bar{position:absolute;height:1.6px;width:10px;background:var(--teal)}
.lorem{position:absolute;font-size:3px;line-height:1.45;color:var(--text)}
.pill{position:absolute;border-radius:6px;font-size:3.6px;font-weight:600;display:flex;align-items:center;justify-content:center;letter-spacing:.6px}
.hero-title{position:absolute;color:#fff;font-weight:700;line-height:1.02}
.footer{position:absolute;left:0;right:0;bottom:0;background:#fff}
.icon-disc{position:absolute;border-radius:50%;background:#fff;display:flex;align-items:center;justify-content:center}
.cell{position:absolute;font-size:2.6px}
</style>
</head>
<body>
<div class="sheet">

<!-- Row 1 -->
<section class="slide" style="left:8px;top:8px">
  <div class="photo" role="img" aria-label="Teal-tinted photo of a person holding a tablet" style="left:0;top:0;width:255px;height:119px;background:linear-gradient(120deg,#0f5f72,#148e9b 60%,#1aa0aa)"></div>
  <div class="hero-title" style="left:12px;top:46px;font-size:13.5px">TITLE OF<br>PRESENTATION</div>
  <div class="a" style="left:13px;top:91px;font-size:3.6px;color:#e6f3f5;line-height:1.35">Here is A place for Credentials<br>Date: 2021 March</div>
  <div class="footer" style="height:24px">
    <div class="brand" style="left:12px;top:10px;color:var(--teal)"><i></i>Lucien Moreau</div>
    <div class="a" style="right:18px;top:10px;font-size:3.8px;font-weight:700;color:var(--navy)">Presenter Name</div>
  </div>
</section>

<section class="slide" style="left:268px;top:8px">
  <div class="photo" role="img" aria-label="Navy-tinted photo of a person holding a tablet" style="left:0;top:0;width:255px;height:119px;background:linear-gradient(120deg,#0c4058,#0b2e48 55%,#08263c)"></div>
  <div class="hero-title" style="left:12px;top:46px;font-size:13.5px">TITLE OF<br>PRESENTATION</div>
  <div class="a" style="left:13px;top:91px;font-size:3.6px;color:#e6f3f5;line-height:1.35">Here is A place for Credentials<br>Date: 2021 March</div>
  <div class="footer" style="height:24px">
    <div class="brand" style="left:12px;top:10px;color:var(--teal)"><i></i>Lucien Moreau</div>
    <div class="a" style="right:18px;top:10px;font-size:3.8px;font-weight:700;color:var(--navy)">Presenter Name</div>
  </div>
</section>

<section class="slide" style="left:528px;top:8px">
  <div class="brand" style="left:17px;top:27px;color:var(--navy)"><i style="background:var(--teal)"></i>Lucien Moreau</div>
  <div class="a" style="left:16px;top:53px;font-size:17px;font-weight:700;color:var(--navy);line-height:.92">Presentation<br>Title Goes Here</div>
  <div class="a" style="left:16px;top:85px;font-size:6px;color:var(--teal)">Sub Title Goes Here</div>
  <div class="pill" style="left:14px;top:112px;width:77px;height:9px;background:var(--teal);color:#fff">www.moreau-conseil.example</div>
</section>

<!-- Row 2 -->
<section class="slide" style="left:8px;top:156px">
  <div class="photo" role="img" aria-label="Teal-toned photo of a business person with a tablet" style="left:0;top:0;width:255px;height:116px;background:linear-gradient(120deg,#0b3048,#0f5d72 50%,#128694)"></div>
  <div class="pill" style="left:79px;top:25px;width:98px;height:8px;background:rgba(255,255,255,.18);color:#fff">www.moreau-conseil.example</div>
  <div class="hero-title center" style="top:46px;font-size:16px">Presentation<br>Title Goes Here</div>
  <div class="a center" style="top:81px;font-size:6px;color:#fff">Sub Title Goes Here</div>
  <div class="pill" style="left:175px;top:110px;width:65px;height:11px;background:var(--teal);color:#fff;letter-spacing:0;font-size:4.6px">Oct 2021</div>
  <div class="brand" style="left:9px;top:128px;color:var(--navy)"><i style="background:var(--teal)"></i>Lucien Moreau</div>
</section>

<section class="slide" style="left:268px;top:156px">
  <div class="photo" role="img" aria-label="Teal-toned photo of a business person with a tablet" style="left:0;top:0;width:255px;height:116px;background:linear-gradient(120deg,#11707f,#138a97 55%,#17a0ab)"></div>
  <div class="pill" style="left:79px;top:25px;width:98px;height:8px;background:rgba(255,255,255,.2);color:#fff">www.moreau-conseil.example</div>
  <div class="hero-title center" style="top:46px;font-size:16px">Presentation<br>Title Goes Here</div>
  <div class="a center" style="top:81px;font-size:6px;color:#fff">Sub Title Goes Here</div>
  <div class="pill" style="left:175px;top:110px;width:65px;height:11px;background:var(--navy);color:#fff;letter-spacing:0;font-size:4.6px">Oct 2021</div>
  <div class="brand" style="left:9px;top:128px;color:var(--navy)"><i style="background:var(--teal)"></i>Lucien Moreau</div>
</section>

<section class="slide" style="left:528px;top:156px">
  <div class="photo" role="img" aria-label="Teal-toned photo of a city skyline" style="left:0;top:0;width:255px;height:143px;background:linear-gradient(180deg,#0d6b7c,#0c4d66 55%,#0a3a55)"></div>
  <div class="brand" style="left:100px;top:30px;color:#fff"><i></i>Lucien Moreau</div>
  <div class="hero-title center" style="top:56px;font-size:16px">Presentation<br>Title Goes Here</div>
  <div class="a center" style="top:89px;font-size:6px;color:#fff">Sub Title Goes Here</div>
  <div class="pill" style="left:80px;top:108px;width:95px;height:8px;background:rgba(255,255,255,.18);color:#fff">www.moreau-conseil.example</div>
</section>

<!-- Row 3 -->
<section class="slide" style="left:8px;top:305px;background:var(--teal)">
  <div class="brand" style="left:30px;top:33px;color:#fff;font-size:3.4px"><i style="width:4px;height:4px"></i>Lucien Moreau</div>
  <div class="a" style="left:16px;top:36px;font-family:'Comfortaa',sans-serif;font-size:34px;color:rgba(255,255,255,.1)">01</div>
  <div class="a" style="left:30px;top:47px;font-family:'Comfortaa',sans-serif;font-size:20px;color:#fff;line-height:.95">Slide<br>Break</div>
  <div class="lorem" style="left:30px;top:90px;width:108px;color:#dff1f3;font-size:3.2px">Lorem ipsum dolor sit amet, consectetur adipiscing elit, sed do eiusmod tempor incididunt ut labore et dolore magna aliqua. Lorem ipsum dolor sit amet, consectetur adipiscing elit, sed do eiusmod tempor incididunt ut labore et dolore magna aliqua.</div>
</section>

<section class="slide" style="left:268px;top:305px;background:var(--navy)">
  <div class="brand" style="left:30px;top:33px;color:#fff;font-size:3.4px"><i style="width:4px;height:4px"></i>Lucien Moreau</div>
  <div class="a" style="left:16px;top:36px;font-family:'Comfortaa',sans-serif;font-size:34px;color:rgba(255,255,255,.08)">01</div>
  <div class="a" style="left:30px;top:47px;font-family:'Comfortaa',sans-serif;font-size:20px;color:#fff;line-height:.95">Slide<br>Break</div>
  <div class="lorem" style="left:30px;top:90px;width:108px;color:#d6e1ea;font-size:3.2px">Lorem ipsum dolor sit amet, consectetur adipiscing elit, sed do eiusmod tempor incididunt ut labore et dolore magna aliqua. Lorem ipsum dolor sit amet, consectetur adipiscing elit, sed do eiusmod tempor incididunt ut labore et dolore magna aliqua.</div>
</section>

<section class="slide" style="left:528px;top:305px">
  <div class="mini-mark"><i></i>Lucien Moreau</div>
  <div class="side-rule"></div><div class="side-label">LUCIEN MOREAU | CONSEIL</div>
  <div class="s-title" style="left:22px;top:14px;font-size:10.5px">Title And Body Slide</div>
  <div class="bar" style="left:23px;top:28px"></div>
</section>

<!-- Row 4 -->
<section class="slide" style="left:8px;top:454px">
  <div class="mini-mark"><i></i>Lucien Moreau</div>
  <div class="side-rule"></div><div class="side-label">LUCIEN MOREAU | CONSEIL</div>
  <div class="s-title" style="left:22px;top:14px;font-size:10.5px">Title And Body Slide</div>
  <div class="bar" style="left:23px;top:28px"></div>
  <div class="lorem" style="left:24px;top:45px;width:212px;font-size:2.9px;text-align:justify">
    <p style="margin-bottom:3px">Lorem ipsum dolor sit amet, consectetur adipiscing elit, sed do eiusmod tempor incididunt ut labore et dolore magna aliqua. Lorem ipsum dolor sit amet, consectetur adipiscing elit, sed do eiusmod tempor incididunt ut labore et dolore magna aliqua. Ut enim ad minim veniam, quis nostrud exercitation ullamco laboris nisi ut aliquip.</p>
    <p style="margin-bottom:3px">Lorem ipsum dolor sit amet, consectetur adipiscing elit. Lorem ipsum dolor sit amet, consectetur adipiscing elit, sed do eiusmod tempor incididunt ut labore et dolore magna aliqua. Lorem ipsum dolor sit amet, consectetur adipiscing elit, sed do eiusmod tempor incididunt ut labore et dolore magna aliqua. Ut enim ad minim veniam, quis nostrud exercitation ullamco laboris nisi ut aliquip.</p>
    <p>Lorem ipsum dolor sit amet, consectetur adipiscing elit, sed do eiusmod tempor incididunt ut labore et dolore magna aliqua. Lorem ipsum dolor sit amet, consectetur adipiscing elit, sed do eiusmod tempor incididunt ut labore et dolore magna aliqua. Sed do eiusmod tempor incididunt ut labore et dolore magna aliqua. Lorem ipsum dolor sit amet, consectetur adipiscing elit, sed do eiusmod tempor incididunt ut labore et dolore magna aliqua. Ut enim ad minim veniam, quis nostrud exercitation ullamco laboris nisi ut aliquip.</p>
  </div>
</section>

<section class="slide" style="left:268px;top:454px">
  <div class="mini-mark"><i></i>Lucien Moreau</div>
  <div class="side-rule"></div><div class="side-label">LUCIEN MOREAU | CONSEIL</div>
  <div class="s-title" style="left:25px;top:37px;font-size:13px">Pic And Text</div>
  <div class="bar" style="left:26px;top:54px"></div>
  <div class="lorem" style="left:25px;top:66px;width:87px;font-size:3.5px;text-align:justify;line-height:1.35">Lorem ipsum dolor sit amet, consectetur adipiscing elit, sed do eiusmod tempor incididunt ut labore et dolore magna aliqua. Lorem ipsum dolor sit amet, consectetur adipiscing elit, sed do eiusmod tempor incididunt ut labore et dolore magna aliqua. Ut enim ad minim veniam, quis nostrud exercitation ullamco laboris nisi ut aliquip.</div>
  <div class="a" style="left:130px;top:33px;width:125px;height:80px;background:linear-gradient(135deg,var(--teal),var(--navy))"></div>
  <div class="photo" role="img" aria-label="Photo of city skyscrapers at sunset" style="left:145px;top:18px;width:110px;height:78px;background:linear-gradient(180deg,#c9d6de,#8e8a7e 55%,#4b4a48)"></div>
</section>

<section class="slide" style="left:528px;top:454px">
  <div class="photo" role="img" aria-label="Photo of a hiker standing on a mountain peak above the clouds" style="left:0;top:0;width:110px;height:143px;background:linear-gradient(180deg,#3e4c59,#7e8a91 45%,#3a3f44)"></div>
  <div class="a" style="left:125px;top:40px;width:28px;height:1.3px;background:var(--teal)"></div>
  <div class="a" style="left:125px;top:44px;width:115px;font-size:6px;font-weight:600;color:var(--navy);line-height:1.25">Success is not only what you achieve in your life, but also what you inspire in the lives of others</div>
  <div class="a" style="left:57px;top:94px;width:198px;height:49px;background:linear-gradient(90deg,var(--teal),var(--navy));border-top-left-radius:6px"></div>
  <div class="a" style="left:74px;top:107px;width:55px;color:#fff"><div style="font-size:3.6px;font-weight:600">Lorem ipsum dolor</div><div style="font-size:2.6px;margin-top:3px;line-height:1.4">Lorem ipsum dolor sit amet, consectetur adipiscing elit, sed do eiusmod tempor</div></div>
  <div class="a" style="left:134px;top:107px;width:55px;color:#fff"><div style="font-size:3.6px;font-weight:600">Lorem ipsum dolor</div><div style="font-size:2.6px;margin-top:3px;line-height:1.4">Lorem ipsum dolor sit amet, consectetur adipiscing elit, sed do eiusmod tempor</div></div>
  <div class="a" style="left:196px;top:107px;width:55px;color:#fff"><div style="font-size:3.6px;font-weight:600">Lorem ipsum dolor</div><div style="font-size:2.6px;margin-top:3px;line-height:1.4">Lorem ipsum dolor sit amet, consectetur adipiscing elit, sed do eiusmod tempor</div></div>
</section>

<!-- Row 5 -->
<section class="slide" style="left:8px;top:602px">
  <div class="mini-mark"><i></i>Lucien Moreau</div>
  <div class="side-rule"></div><div class="side-label">LUCIEN MOREAU | CONSEIL</div>
  <div class="page-no">13</div>
  <div class="a" style="left:12.5px;top:0;width:242.5px;height:60px;background:var(--navy)"></div>
  <div class="s-title center" style="left:12px;top:20px;font-size:11px;color:#fff">Here Add Awesome Text</div>
  <div class="bar" style="left:128px;top:36px;width:12px"></div>
  <svg class="a" style="left:12px;top:0" width="243" height="143" viewBox="0 0 243 143">
    <g fill="var(--teal)" stroke="#fff" stroke-width="1.4">
      <circle cx="55" cy="71" r="13"/><circle cx="126" cy="71" r="13"/><circle cx="196" cy="71" r="13"/>
    </g>
    <g fill="none" stroke="#fff" stroke-width=".7">
      <circle cx="55" cy="71" r="5"/><circle cx="55" cy="71" r="2.5"/><path d="M55 71l6-5"/>
      <path d="M121 76l8-9 3-1-1 3-9 8z M121 76l-2 2"/>
      <path d="M190 76v-4M194 76v-7M198 76v-5M202 76v-9M189 70l5-4 4 2 5-5"/>
    </g>
  </svg>
  <div class="a" style="left:33px;top:88px;width:68px;text-align:center"><div style="font-size:4.4px;font-weight:600">Project name</div><div style="font-size:2.8px;color:var(--text);margin-top:2px;line-height:1.35">Lorem ipsum dolor sit amet, nec an dictas equidem appellantur, ut has commune accommodare. Mea illum, ludus solet idpro.</div></div>
  <div class="a" style="left:104px;top:88px;width:68px;text-align:center"><div style="font-size:4.4px;font-weight:600">Project name</div><div style="font-size:2.8px;color:var(--text);margin-top:2px;line-height:1.35">Lorem ipsum dolor sit amet, nec an dictas equidem appellantur, ut has commune accommodare. Mea illum, ludus solet idpro.</div></div>
  <div class="a" style="left:174px;top:88px;width:68px;text-align:center"><div style="font-size:4.4px;font-weight:600">Project name</div><div style="font-size:2.8px;color:var(--text);margin-top:2px;line-height:1.35">Lorem ipsum dolor sit amet, nec an dictas equidem appellantur, ut has commune accommodare. Mea illum, ludus solet idpro.</div></div>
</section>

<section class="slide" style="left:268px;top:602px">
  <div class="mini-mark"><i></i>Lucien Moreau</div>
  <div class="side-rule"></div><div class="side-label">LUCIEN MOREAU | CONSEIL</div>
  <div class="s-title center" style="top:16px;font-size:11px">3 Columns Slide</div>
  <div class="bar" style="left:122px;top:31px;width:11px"></div>
  <div class="a" style="left:35px;top:59px;width:58px;height:51px;border-radius:2px;background:var(--teal)"></div>
  <div class="a" style="left:100px;top:59px;width:58px;height:51px;border-radius:2px;background:var(--navy)"></div>
  <div class="a" style="left:165px;top:59px;width:58px;height:51px;border-radius:2px;background:var(--grey)"></div>
  <svg class="a" style="left:0;top:0" width="255" height="143" viewBox="0 0 255 143">
    <g fill="#fff" stroke="#e4e4e4" stroke-width=".5"><circle cx="64" cy="59" r="10"/><circle cx="129" cy="59" r="10"/><circle cx="194" cy="59" r="10"/></g>
    <g fill="none" stroke-width=".7">
      <g stroke="var(--teal)"><circle cx="64" cy="59" r="2.5"/><path d="M64 53v3.5M64 61.5V65M58 59h3.5M66.5 59H70M60 55l2 2M68 63l-2-2M68 55l-2 2M60 63l2-2"/></g>
      <g stroke="var(--navy)"><circle cx="129" cy="59" r="5"/><circle cx="129" cy="59" r="2.5"/></g>
      <g stroke="var(--grey)"><circle cx="194" cy="56" r="2"/><circle cx="190" cy="62" r="2"/><circle cx="198" cy="62" r="2"/><path d="M194 58l-3 2M194 58l3 2"/></g>
    </g>
  </svg>
  <div class="a" style="left:37px;top:74px;width:54px;text-align:center;color:#fff"><div style="font-size:3.8px;font-weight:600">Project name here</div><div style="font-size:2.7px;margin-top:2px;line-height:1.35">Lorem ipsum dolor sit amet, nec an dictas equidem appellantur, ut has commune accommodare. Mea illum, ludus solet idpro.</div></div>
  <div class="a" style="left:102px;top:74px;width:54px;text-align:center;color:#fff"><div style="font-size:3.8px;font-weight:600">Project name here</div><div style="font-size:2.7px;margin-top:2px;line-height:1.35">Lorem ipsum dolor sit amet, nec an dictas equidem appellantur, ut has commune accommodare. Mea illum, ludus solet idpro.</div></div>
  <div class="a" style="left:167px;top:74px;width:54px;text-align:center;color:#fff"><div style="font-size:3.8px;font-weight:600">Project name here</div><div style="font-size:2.7px;margin-top:2px;line-height:1.35">Lorem ipsum dolor sit amet, nec an dictas equidem appellantur, ut has commune accommodare. Mea illum, ludus solet idpro.</div></div>
</section>

<section class="slide" style="left:528px;top:602px">
  <div class="mini-mark"><i></i>Lucien Moreau</div>
  <div class="side-rule"></div><div class="side-label">LUCIEN MOREAU | CONSEIL</div>
  <div class="s-title center" style="top:12px;font-size:11px">6 Columns Slide</div>
  <div class="bar" style="left:122px;top:27px;width:11px"></div>
  <svg class="a" style="left:0;top:0" width="255" height="143" viewBox="0 0 255 143">
    <g fill="#fff" stroke="#e4e4e4" stroke-width=".5">
      <circle cx="29" cy="52" r="6"/><circle cx="29" cy="79" r="6"/><circle cx="29" cy="106" r="6"/>
      <circle cx="140" cy="52" r="6"/><circle cx="140" cy="79" r="6"/><circle cx="140" cy="106" r="6"/>
    </g>
    <g fill="none" stroke="var(--navy)" stroke-width=".6">
      <rect x="26.5" y="48.5" width="5" height="7"/><path d="M27.5 50.5h3M27.5 52.5h3M27.5 54h3"/>
      <rect x="137.5" y="48.5" width="5" height="7"/><path d="M138.5 50.5h3M138.5 52.5h3M138.5 54h3"/>
      <path d="M26 82v-2M28 82v-3M30 82v-4M32 82v-6"/><path d="M137 82v-2M139 82v-3M141 82v-4M143 82v-6"/>
      <circle cx="28" cy="105" r="2"/><path d="M25 109c0-2 6-2 6 0M31 103l2-2"/><circle cx="139" cy="105" r="2"/><path d="M136 109c0-2 6-2 6 0M142 103l2-2"/>
    </g>
  </svg>
  <div class="a" style="left:43px;top:44px;width:70px"><div style="font-size:3.4px;font-weight:600;color:var(--teal)">Project name</div><div style="font-size:2.6px;color:var(--text);line-height:1.3;margin-top:1px">Lorem ipsum dolor sit amet, nec an dictas equidem appellantur, ut commune accommodare. Mea illum, ludus solet idpro.</div></div>
  <div class="a" style="left:43px;top:71px;width:70px"><div style="font-size:3.4px;font-weight:600;color:var(--teal)">Project name</div><div style="font-size:2.6px;color:var(--text);line-height:1.3;margin-top:1px">Lorem ipsum dolor sit amet, nec an dictas equidem appellantur, ut has commune accommodare. Mea illum, ludus solet idpro.</div></div>
  <div class="a" style="left:43px;top:98px;width:70px"><div style="font-size:3.4px;font-weight:600;color:var(--teal)">Project name</div><div style="font-size:2.6px;color:var(--text);line-height:1.3;margin-top:1px">Lorem ipsum dolor sit amet, nec an dictas equidem appellantur, ut has commune accommodare. Mea illum, ludus solet idpro.</div></div>
  <div class="a" style="left:154px;top:44px;width:70px"><div style="font-size:3.4px;font-weight:600;color:var(--teal)">Project name</div><div style="font-size:2.6px;color:var(--text);line-height:1.3;margin-top:1px">Lorem ipsum dolor sit amet, nec an dictas equidem appellantur, ut has commune accommodare. Mea illum, ludus solet idpro.</div></div>
  <div class="a" style="left:154px;top:71px;width:70px"><div style="font-size:3.4px;font-weight:600;color:var(--teal)">Project name</div><div style="font-size:2.6px;color:var(--text);line-height:1.3;margin-top:1px">Lorem ipsum dolor sit amet, nec an dictas equidem appellantur, ut has commune accommodare. Mea illum, ludus solet idpro.</div></div>
  <div class="a" style="left:154px;top:98px;width:70px"><div style="font-size:3.4px;font-weight:600;color:var(--teal)">Project name</div><div style="font-size:2.6px;color:var(--text);line-height:1.3;margin-top:1px">Lorem ipsum dolor sit amet, nec an dictas equidem appellantur, ut has commune accommodare. Mea illum, ludus solet idpro.</div></div>
</section>

<!-- Row 6 -->
<section class="slide" style="left:8px;top:751px">
  <div class="mini-mark"><i></i>Lucien Moreau</div>
  <div class="side-rule"></div><div class="side-label">LUCIEN MOREAU | CONSEIL</div>
  <div class="s-title center" style="left:12px;top:11px;font-size:11px">Chart Slide</div>
  <div class="bar" style="left:124px;top:26px;width:11px"></div>
  <svg class="a" style="left:0;top:0" width="255" height="143" viewBox="0 0 255 143" font-family="Montserrat, sans-serif">
    <rect x="82" y="34" width="155" height="11" rx="1.5" fill="var(--teal)"/>
    <g fill="#fff" font-size="3" font-weight="600" text-anchor="middle"><text x="102" y="40.5">Your Text Here</text><text x="140" y="40.5">Your Text Here</text><text x="179" y="40.5">Your Text Here</text><text x="218" y="40.5">Your Text Here</text></g>
    <rect x="20" y="45" width="62" height="77" fill="var(--navy)"/>
    <g fill="#f3f5f6"><rect x="82" y="45" width="155" height="11"/><rect x="82" y="67" width="155" height="11"/><rect x="82" y="89" width="155" height="11"/><rect x="82" y="111" width="155" height="11"/></g>
    <g stroke="#3a5770" stroke-width=".3"><path d="M20 56h62M20 67h62M20 78h62M20 89h62M20 100h62M20 111h62"/></g>
    <g fill="#fff" font-size="3" font-weight="600" text-anchor="middle">
      <text x="51" y="52">You can replace this text</text><text x="51" y="63">You can replace this text</text><text x="51" y="74">You can replace this text</text><text x="51" y="85">You can replace this text</text><text x="51" y="96">You can replace this text</text><text x="51" y="107">You can replace this text</text><text x="51" y="118">You can replace this text</text>
    </g>
    <g fill="#777" font-size="2.8" text-anchor="middle">
      <text x="102" y="52">1250</text><text x="102" y="63">3623</text><text x="102" y="74">2569</text><text x="102" y="85">1020</text><text x="102" y="96">2320</text><text x="102" y="107">5698</text><text x="102" y="118">1999</text>
      <text x="179" y="52">50%</text><text x="179" y="63">50%</text><text x="179" y="74">12%</text><text x="179" y="85">65%</text><text x="179" y="96">36%</text><text x="179" y="107">95%</text><text x="179" y="118">66%</text>
      <text x="218" y="52">1250</text><text x="218" y="63">3623</text><text x="218" y="74">2569</text><text x="218" y="85">1020</text><text x="218" y="96">2320</text><text x="218" y="107">5698</text><text x="218" y="118">1999</text>
    </g>
    <g fill="none" stroke-width="1.1" stroke-linecap="round">
      <path d="M138 50.5l1.5 1.5 3-3.5M138 72.5l1.5 1.5 3-3.5M138 94.5l1.5 1.5 3-3.5" stroke="var(--teal)"/>
      <path d="M138.5 59l3 3M141.5 59l-3 3M138.5 81l3 3M141.5 81l-3 3M138.5 103l3 3M141.5 103l-3 3M138.5 114l3 3M141.5 114l-3 3" stroke="var(--navy)"/>
    </g>
  </svg>
</section>

<section class="slide" style="left:268px;top:751px">
  <div class="mini-mark"><i></i>Lucien Moreau</div>
  <div class="side-rule"></div><div class="side-label">LUCIEN MOREAU | CONSEIL</div>
  <div class="s-title" style="left:22px;top:14px;font-size:11px">Smart Art Slide</div>
  <div class="bar" style="left:23px;top:29px"></div>
  <svg class="a" style="left:0;top:0" width="255" height="143" viewBox="0 0 255 143">
    <g fill="none" stroke="var(--teal)" stroke-width=".6"><circle cx="29" cy="57" r="3"/><circle cx="29" cy="57" r="1.5"/><path d="M25 86l6-6 1 1-6 6zM25 115h6v-5h-6zM27 112h2"/></g>
    <defs><linearGradient id="tri" x1="0" y1="0" x2="0" y2="1"><stop offset="0" stop-color="var(--teal)"/><stop offset="1" stop-color="var(--navy)"/></linearGradient></defs>
    <path d="M186 35l24 44c1 2 0 3-2 3h-44c-2 0-3-1-2-3z" fill="url(#tri)"/>
    <path d="M159 84l26 42c1 1 0 2-2 2h-48c-2 0-2-1-1-2z" fill="url(#tri)"/>
    <path d="M214 84l26 42c1 1 0 2-2 2h-48c-2 0-2-1-1-2z" fill="url(#tri)"/>
  </svg>
  <div class="a" style="left:37px;top:50px;width:80px"><div style="font-size:3.6px;font-weight:600">Lorem ipsum dolor</div><div style="font-size:2.6px;color:var(--text);line-height:1.35">Lorem ipsum dolor sit amet, consectetur adipiscing elit, sed do eiusmod tempor eta beta on lipon eterim dolor sin ter ti.</div></div>
  <div class="a" style="left:37px;top:79px;width:80px"><div style="font-size:3.6px;font-weight:600">Lorem ipsum dolor</div><div style="font-size:2.6px;color:var(--text);line-height:1.35">Lorem ipsum dolor sit amet, consectetur adipiscing elit, sed do eiusmod tempor eta beta on lipon eterim dolor sin ter ti.</div></div>
  <div class="a" style="left:37px;top:108px;width:80px"><div style="font-size:3.6px;font-weight:600">Lorem ipsum dolor</div><div style="font-size:2.6px;color:var(--text);line-height:1.35">Lorem ipsum dolor sit amet, consectetur adipiscing elit, sed do eiusmod tempor eta beta on lipon eterim dolor sin ter ti.</div></div>
  <div class="a" style="left:173px;top:53px;width:26px;text-align:center;color:#fff"><div style="font-size:3.2px;font-weight:600">Project name</div><div style="font-size:2.2px;line-height:1.3;margin-top:1px">Lorem ipsum dolor sit amet nec an dictas equidem appellantur, ut has commune</div></div>
  <div class="a" style="left:144px;top:102px;width:30px;text-align:center;color:#fff"><div style="font-size:3.2px;font-weight:600">Project name</div><div style="font-size:2.2px;line-height:1.3;margin-top:1px">Lorem ipsum dolor sit amet nec an dictas equidem appellantur, ut has commune</div></div>
  <div class="a" style="left:199px;top:102px;width:30px;text-align:center;color:#fff"><div style="font-size:3.2px;font-weight:600">Project name</div><div style="font-size:2.2px;line-height:1.3;margin-top:1px">Lorem ipsum dolor sit amet nec an dictas equidem appellantur, ut has commune</div></div>
</section>

<section class="slide" style="left:528px;top:751px">
  <div class="mini-mark"><i></i>Lucien Moreau</div>
  <div class="side-rule"></div><div class="side-label">LUCIEN MOREAU | CONSEIL</div>
  <div class="page-no">18</div>
  <div class="s-title center" style="top:11px;font-size:11px">Here is Quotes</div>
  <div class="bar" style="left:122px;top:26px;width:11px"></div>
  <div class="a" style="left:25px;top:36px;font-size:20px;font-weight:800;color:var(--teal);line-height:1">”</div>
  <div class="a" style="left:142px;top:36px;font-size:20px;font-weight:800;color:var(--teal);line-height:1">”</div>
  <div class="a" style="left:25px;top:61px;width:92px;font-size:3.8px;line-height:1.5;color:var(--text)">Lorem ipsum dolor sit amet, consectetur adipiscing elit, sed do eiusmod tempor incididunt ut labore et dolore magna aliqua. Lorem ipsum dolor sit amet, consectetur adipiscing elit.</div>
  <div class="a" style="left:142px;top:61px;width:92px;font-size:3.8px;line-height:1.5;color:var(--text)">Lorem ipsum dolor sit amet, consectetur adipiscing elit, sed do eiusmod tempor incididunt ut labore et dolore magna aliqua. Lorem ipsum dolor sit amet, consectetur adipiscing elit.</div>
  <svg class="a" style="left:0;top:0" width="255" height="143" viewBox="0 0 255 143"><g fill="#ddd"><circle cx="32" cy="108" r="6.5"/><circle cx="149" cy="108" r="6.5"/></g></svg>
  <div class="a" style="left:43px;top:104px;font-size:3.6px;line-height:1.4"><div style="color:var(--teal);font-weight:600">Your Name</div><div style="color:var(--text)">Founder</div></div>
  <div class="a" style="left:160px;top:104px;font-size:3.6px;line-height:1.4"><div style="color:var(--teal);font-weight:600">Your Name</div><div style="color:var(--text)">Founder</div></div>
</section>

<!-- Row 7 -->
<section class="slide" style="left:8px;top:900px">
  <div class="mini-mark"><i></i>Lucien Moreau</div>
  <div class="side-rule"></div><div class="side-label">LUCIEN MOREAU | CONSEIL</div>
  <div class="s-title center" style="left:12px;top:14px;font-size:11px">Here Is Statistics</div>
  <div class="bar" style="left:124px;top:29px;width:11px"></div>
  <svg class="a" style="left:0;top:0" width="255" height="143" viewBox="0 0 255 143" font-family="Montserrat, sans-serif">
    <circle cx="58" cy="85" r="37" fill="var(--navy)"/>
    <circle cx="58" cy="97" r="25" fill="var(--teal)"/>
    <circle cx="58" cy="109" r="13" fill="#5a5a5a"/>
    <g fill="#fff" font-weight="700" text-anchor="middle"><text x="58" y="65" font-size="10">$</text><text x="58" y="87" font-size="9">$</text><text x="58" y="113" font-size="7">$</text></g>
    <g stroke="#bbb" stroke-width=".4"><path d="M66 61h43M80 83h29M70 110h39"/></g>
    <g fill="var(--navy)" font-size="6" font-weight="600"><text x="112" y="63">5M</text><text x="112" y="85">2M</text><text x="112" y="112">1M</text></g>
    <g fill="var(--navy)"><rect x="146" y="59" width="9" height="9"/><rect x="146" y="82" width="9" height="9" fill="var(--teal)"/><rect x="146" y="105" width="9" height="9" fill="#555"/></g>
    <g fill="none" stroke="#fff" stroke-width="1"><path d="M148 63.5l2 2 3-4M148 86.5l2 2 3-4M148 109.5l2 2 3-4"/></g>
  </svg>
  <div class="a" style="left:159px;top:56px;width:80px"><div style="font-size:4px;font-weight:600">Lorem ipsum dolor</div><div style="font-size:2.9px;color:var(--text);line-height:1.35;margin-top:1px">Lorem ipsum dolor sit amet, consectetur adipiscing elit, sed do eiusmod tempor</div></div>
  <div class="a" style="left:159px;top:79px;width:80px"><div style="font-size:4px;font-weight:600">Lorem ipsum dolor</div><div style="font-size:2.9px;color:var(--text);line-height:1.35;margin-top:1px">Lorem ipsum dolor sit amet, consectetur adipiscing elit, sed do eiusmod tempor</div></div>
  <div class="a" style="left:159px;top:102px;width:80px"><div style="font-size:4px;font-weight:600">Lorem ipsum dolor</div><div style="font-size:2.9px;color:var(--text);line-height:1.35;margin-top:1px">Lorem ipsum dolor sit amet, consectetur adipiscing elit, sed do eiusmod tempor</div></div>
</section>

<section class="slide" style="left:268px;top:900px">
  <div class="mini-mark"><i></i>Lucien Moreau</div>
  <div class="side-rule"></div><div class="side-label">LUCIEN MOREAU | CONSEIL</div>
  <div class="s-title center" style="top:14px;font-size:11px">Here Add Your Title</div>
  <div class="bar" style="left:122px;top:29px;width:11px"></div>
  <div class="a" style="left:48px;top:40px;width:160px;text-align:center;font-size:3.1px;line-height:1.45;color:var(--text)">Lorem Ipsum the printing and typesetting industry. Lorem Ipsum has been the industry's standard dummy text ever since the 1500s, when an unknown printer took a galley of type and scrambled it to make a type specimen book. It has survived not only five centuries.</div>
  <svg class="a" style="left:0;top:0" width="255" height="143" viewBox="0 0 255 143" font-family="Montserrat, sans-serif">
    <g fill="none" stroke-width="1.8">
      <circle cx="72" cy="86" r="17" stroke="#eee"/><circle cx="72" cy="86" r="17" stroke="#555" stroke-dasharray="53.4 106.8" transform="rotate(-90 72 86)"/>
      <circle cx="126" cy="86" r="17" stroke="#eee"/><circle cx="126" cy="86" r="17" stroke="var(--navy)" stroke-dasharray="80.1 106.8" transform="rotate(-90 126 86)"/>
      <circle cx="179" cy="86" r="17" stroke="#eee"/><circle cx="179" cy="86" r="17" stroke="var(--teal)" stroke-dasharray="42.7 106.8" transform="rotate(-90 179 86)"/>
    </g>
    <g font-size="8" font-weight="700" text-anchor="middle" fill="var(--navy)"><text x="72" y="89">50%</text><text x="126" y="89">75%</text><text x="179" y="89">40%</text></g>
    <g font-size="2.8" fill="#777" text-anchor="middle">
      <text x="72" y="113">Lorem ipsom dolor amet</text><text x="72" y="117">amet consectetur dolor</text>
      <text x="126" y="113">Lorem ipsom dolor amet</text><text x="126" y="117">amet consectetur dolor</text>
      <text x="179" y="113">Lorem ipsom dolor amet</text><text x="179" y="117">amet consectetur dolor</text>
    </g>
  </svg>
</section>

<section class="slide" style="left:528px;top:900px">
  <div class="mini-mark"><i></i>Lucien Moreau</div>
  <div class="side-rule"></div><div class="side-label">LUCIEN MOREAU | CONSEIL</div>
  <div class="page-no">21</div>
  <div class="s-title center" style="top:12px;font-size:11px">Here is Statistics</div>
  <div class="bar" style="left:122px;top:27px;width:11px"></div>
  <div class="a" style="left:18px;top:45px;width:62px;height:37px;background:var(--teal);color:#fff;text-align:center">
    <div style="font-size:10px;margin-top:9px">$0.5M</div><div style="font-size:3px;opacity:.8">Revenue</div>
  </div>
  <div class="a" style="left:18px;top:82px;width:62px;height:39px;background:#fff;box-shadow:0 0 3px rgba(0,0,0,.15);color:var(--teal);text-align:center">
    <div style="font-size:9.5px;margin-top:11px">-0.28%</div><div style="font-size:3px;opacity:.8">Revenue</div>
  </div>
  <svg class="a" style="left:0;top:0" width="255" height="143" viewBox="0 0 255 143" font-family="Montserrat, sans-serif">
    <g stroke="#eee" stroke-width=".3"><path d="M108 47h134M108 57h134M108 66h134M108 76h134M108 85h134M108 95h134M108 105h134M108 114h134"/></g>
    <g fill="#777" font-size="2.3" text-anchor="end"><text x="106" y="48">$350,000</text><text x="106" y="58">$300,000</text><text x="106" y="67">$250,000</text><text x="106" y="77">$200,000</text><text x="106" y="86">$150,000</text><text x="106" y="96">$100,000</text><text x="106" y="106">$50,000</text><text x="106" y="115">$-</text></g>
    <g fill="#777" font-size="2.3" text-anchor="middle"><text x="110" y="120">Jan</text><text x="120.5" y="120">Feb</text><text x="131" y="120">Mar</text><text x="141.5" y="120">Apr</text><text x="152" y="120">May</text><text x="162.5" y="120">Jun</text><text x="173" y="120">Jul</text><text x="183.5" y="120">Aug</text><text x="194" y="120">Sep</text><text x="204.5" y="120">Oct</text><text x="215" y="120">Nov</text><text x="225.5" y="120">Dec</text><text x="236" y="120">Jan</text></g>
    <path d="M110 112c8-2 14-4 20-6c6-8 6-22 12-18c5 3 4 6 10-4c8-6 12-2 20-2c8 2 8 10 14 8c6-2 6-10 12-4c6 6 6-16 12-16c4 0 6-10 10-16" fill="none" stroke="var(--teal)" stroke-width=".8"/>
  </svg>
</section>

<!-- Row 8 -->
<section class="slide" style="left:8px;top:1049px">
  <div class="mini-mark"><i></i>Lucien Moreau</div>
  <div class="side-rule"></div><div class="side-label">LUCIEN MOREAU | CONSEIL</div>
  <div class="s-title center" style="left:12px;top:12px;font-size:11px">Company Timeline</div>
  <div class="bar" style="left:124px;top:27px;width:11px"></div>
  <svg class="a" style="left:0;top:0" width="255" height="143" viewBox="0 0 255 143" font-family="Montserrat, sans-serif">
    <g fill="var(--teal)">
      <path d="M23 48h34l9 12-9 12H23l9-12z"/><path d="M63 48h34l9 12-9 12H63l9-12z"/><path d="M103 48h34l9 12-9 12h-34l9-12z"/><path d="M143 48h34l9 12-9 12h-34l9-12z"/><path d="M183 48h44l9 12-9 12h-44l9-12z"/>
    </g>
    <g fill="#fff" font-size="5.4" font-weight="600" text-anchor="middle"><text x="52" y="62">STEP 01</text><text x="92" y="62">STEP 02</text><text x="132" y="62">STEP 03</text><text x="172" y="62">STEP 04</text><text x="214" y="62">STEP 05</text></g>
    <path d="M30 78h210" stroke="#ccc" stroke-width=".4"/>
    <g stroke="#bbb" stroke-width=".4" fill="#fff"><path d="M51 78v8M93 78v8M135 78v8M175 78v8M217 78v8"/><circle cx="51" cy="87" r="1"/><circle cx="93" cy="87" r="1"/><circle cx="135" cy="87" r="1"/><circle cx="175" cy="87" r="1"/><circle cx="217" cy="87" r="1"/></g>
  </svg>
  <div class="a" style="left:31px;top:95px;width:40px;text-align:center"><div style="font-size:4px;font-weight:600">Project name</div><div style="font-size:2.6px;color:var(--text);line-height:1.35;margin-top:2px">Lorem Ipsum is simply dummy unknown printer took a galley of type and scrambled it to make.</div></div>
  <div class="a" style="left:73px;top:95px;width:40px;text-align:center"><div style="font-size:4px;font-weight:600">Project name</div><div style="font-size:2.6px;color:var(--text);line-height:1.35;margin-top:2px">Lorem Ipsum is simply dummy unknown printer took a galley of type and scrambled it to make.</div></div>
  <div class="a" style="left:115px;top:95px;width:40px;text-align:center"><div style="font-size:4px;font-weight:600">Project name</div><div style="font-size:2.6px;color:var(--text);line-height:1.35;margin-top:2px">Lorem Ipsum is simply dummy unknown printer took a galley of type and scrambled it to make.</div></div>
  <div class="a" style="left:155px;top:95px;width:40px;text-align:center"><div style="font-size:4px;font-weight:600">Project name</div><div style="font-size:2.6px;color:var(--text);line-height:1.35;margin-top:2px">Lorem Ipsum is simply dummy unknown printer took a galley of type and scrambled it to make.</div></div>
  <div class="a" style="left:197px;top:95px;width:40px;text-align:center"><div style="font-size:4px;font-weight:600">Project name</div><div style="font-size:2.6px;color:var(--text);line-height:1.35;margin-top:2px">Lorem Ipsum is simply dummy unknown printer took a galley of type and scrambled it to make.</div></div>
</section>

<section class="slide" style="left:268px;top:1049px">
  <div class="mini-mark"><i></i>Lucien Moreau</div>
  <div class="side-rule"></div><div class="side-label">LUCIEN MOREAU | CONSEIL</div>
  <div class="page-no">23</div>
  <div class="s-title center" style="top:14px;font-size:11px">Timeline</div>
  <div class="bar" style="left:124px;top:29px;width:11px"></div>
  <svg class="a" style="left:0;top:0" width="255" height="143" viewBox="0 0 255 143" font-family="Montserrat, sans-serif">
    <rect x="61" y="48" width="180" height="8" fill="var(--teal)"/>
    <g fill="#fff" font-size="2.6" text-anchor="middle">
      <text x="67.4" y="53">S</text><text x="80.3" y="53">M</text><text x="93.1" y="53">T</text><text x="106" y="53">W</text><text x="118.9" y="53">T</text><text x="131.7" y="53">F</text><text x="144.6" y="53">S</text><text x="157.4" y="53">S</text><text x="170.3" y="53">M</text><text x="183.1" y="53">T</text><text x="196" y="53">W</text><text x="208.9" y="53">T</text><text x="221.7" y="53">F</text>
    </g>
    <g fill="#f4f6f7"><rect x="25" y="64.5" width="216" height="8.5"/><rect x="25" y="81.5" width="216" height="8.5"/><rect x="25" y="98.5" width="216" height="8.5"/><rect x="25" y="115.5" width="216" height="8.5"/></g>
    <g fill="var(--navy)" font-size="2.6" font-weight="600">
      <text x="27" y="63">First Task</text><text x="27" y="71.5">Second Task</text><text x="27" y="80">Third Task</text><text x="27" y="88.5">Fourth Task</text><text x="27" y="97">Fifth Task</text><text x="27" y="105.5">Sixth Task</text><text x="27" y="114">Seventh Task</text><text x="27" y="122.5">Eighth Task</text>
    </g>
    <g stroke="var(--navy)" stroke-width="2.8" stroke-linecap="round">
      <path d="M71 62h45M105 70.5h35M159 70.5h35M105 79h51M94 87.5h58M130 96h70M118 104.5h70M78 113h23M214 121.5h24"/>
    </g>
  </svg>
</section>

<section class="slide" style="left:528px;top:1049px;background:#f7f8f9">
  <div class="a" role="img" aria-label="Faint architectural background pattern" style="left:0;top:0;width:255px;height:143px;background:linear-gradient(135deg,#f9fafa,#eef1f2)"></div>
  <div class="a" style="left:35px;top:37px;width:67px;height:16px;background:var(--teal)"></div>
  <div class="a" style="left:35px;top:55px;width:67px;height:17px;background:#fff"></div>
  <div class="a" style="left:35px;top:74px;width:67px;height:16px;background:#fff"></div>
  <div class="a" style="left:35px;top:92px;width:67px;height:16px;background:#fff"></div>
  <svg class="a" style="left:0;top:0" width="255" height="143" viewBox="0 0 255 143">
    <g fill="none" stroke="#fff" stroke-width=".6"><circle cx="44" cy="45" r="3"/><path d="M41 45h6M44 42c-1.5 2-1.5 4 0 6M44 42c1.5 2 1.5 4 0 6"/></g>
    <g fill="var(--teal)">
      <path d="M44 59a2.6 2.6 0 0 1 2.6 2.6c0 2-2.6 4.4-2.6 4.4s-2.6-2.4-2.6-4.4A2.6 2.6 0 0 1 44 59zm0 1.7a.9.9 0 1 0 0 1.8.9.9 0 0 0 0-1.8z"/>
      <path d="M42 79.5c.5-.5 1.2-.5 1.5 0l.7 1c.2.4 0 .8-.3 1 .5 1 1.2 1.7 2.2 2.2.2-.3.6-.5 1-.3l1 .7c.5.3.5 1 0 1.5-.8.8-2 .8-3 .2-1.8-1-3-2.3-3.8-4-.4-.8-.2-1.6.7-2.3z"/>
      <rect x="41" y="97.5" width="6" height="4.5" rx=".5"/>
    </g>
    <path d="M41 97.8l3 2.4 3-2.4" fill="none" stroke="#fff" stroke-width=".5"/>
    <g fill="var(--teal)"><rect x="53" y="115" width="5" height="5" rx="1"/><rect x="60" y="115" width="5" height="5" rx="1"/><rect x="67" y="115" width="5" height="5" rx="1"/><rect x="74" y="115" width="5" height="5" rx="1"/></g>
  </svg>
  <div class="a" style="left:53px;top:43.5px;font-size:2.8px;color:#fff">www.moreau-conseil.example</div>
  <div class="a" style="left:53px;top:59px;font-size:2.8px;color:var(--text);line-height:1.4">Here to write your<br>Company adress</div>
  <div class="a" style="left:53px;top:80.5px;font-size:2.8px;color:var(--text)">(555) 010-0199</div>
  <div class="a" style="left:53px;top:98.5px;font-size:2.8px;color:var(--text)">info@moreau-conseil.example</div>
  <div class="a" style="left:137px;top:62px;font-size:15px;font-weight:700;color:var(--teal)">Thank You</div>
</section>

</div>
</body>
</html>
```